Stress Coach website development

Need a website designed for a coaching business. Very high-end, luxury, professionalism, in the area of STRESS, see brief attached. I have a logo already
Updates

Slow in providing feedback

Target Market(s)

CEOs very successful men and wealthy females, high end luxury market

Industry/Entity Type

coaching

Number of Pages Required

1 page

Requirements
Must have
• Luxury look, professional, serious but warm, appealing to both sexes

```html
<!DOCTYPE html>
<html lang="en">
<head>
<meta charset="utf-8">
<title>Steady Mind — Stress Coaching</title>
<link href="https://fonts.googleapis.com/css2?family=Roboto:wght@400;500;700&family=Mulish:wght@400;600;700&display=swap" rel="stylesheet">
<style>
:root{
  --canvas:#e4e4e4;
  --ink:#231f20;
  --dark:#221f20;
  --yellow:#f7e03a;
  --yellow-deep:#e3c51a;
  --white:#ffffff;
  --card:#bfbfbf;
  --band:#c6c6c6;
  --sky:#cddcf2;
  --quote:#2f86d6;
  --muted:#555;
  --field:#e6e6e6;
}
*{margin:0;padding:0;box-sizing:border-box}
html,body{width:1200px;height:1200px;overflow:hidden;background:var(--canvas)}
body{position:relative;font-family:'Mulish',sans-serif;color:var(--ink)}
.page{position:absolute;left:402.5px;top:0;width:640px;height:1932px;background:var(--white);transform:scale(0.6211);transform-origin:0 0;overflow:hidden}
.abs{position:absolute}
.head{font-family:'Roboto',sans-serif}

/* header */
.site-header{left:0;top:0;width:640px;height:51px;background:var(--dark)}
.brand{left:45px;top:19px;display:flex;align-items:center;gap:7px;color:var(--white);font-family:'Mulish',sans-serif;font-weight:700;font-size:6.5px;letter-spacing:2.2px}
.brand-mark{width:13px;height:13px;border-radius:50%;background:var(--white)}
.nav{top:24px;font-size:7.5px;color:var(--white);font-family:'Roboto',sans-serif}
.nav-active::after{content:"";position:absolute;left:0;top:14px;width:25px;height:2px;background:var(--yellow)}

/* hero */
.hero{left:0;top:51px;width:640px;height:259px;background:linear-gradient(180deg,#b7cdee 0%,#9fb9e4 55%,#a9bfe3 100%)}
.hero-rule{left:0;top:310px;width:640px;height:3px;background:var(--yellow)}
.hero-kicker{left:0;width:640px;text-align:center;color:var(--white);font-family:'Roboto',sans-serif;font-size:16px;letter-spacing:4px}
.hero-title{left:0;top:145px;width:640px;text-align:center;color:var(--yellow);font-family:'Roboto',sans-serif;font-weight:700;font-size:40px;letter-spacing:8px}
.hero-cta{left:267px;top:224px;width:106px;height:22px;border:1.5px solid var(--yellow);border-radius:11px;color:var(--yellow);font-size:7px;text-align:center;line-height:19px;letter-spacing:.5px}

/* welcome */
.section-title{left:0;width:640px;text-align:center;font-family:'Roboto',sans-serif;font-weight:500;font-size:21px;color:var(--ink)}
.intro{left:48px;top:410px;width:545px;font-size:6.3px;line-height:10px;color:#333}
.intro p{margin-bottom:10px}

/* coach */
.coach-photo{left:46px;top:572px;width:278px;height:240px;background:linear-gradient(135deg,#8a8a8a,#4a4a4a 60%,#2e2e2e)}
.coach-panel{left:324px;top:572px;width:270px;height:240px;background:var(--dark);color:var(--white)}
.coach-name{left:20px;top:13px;color:var(--yellow);font-family:'Roboto',sans-serif;font-weight:500;font-size:21px}
.coach-text{left:23px;width:232px;font-size:6.3px;line-height:10px}
.pill-outline{border:1.5px solid var(--yellow);border-radius:11px;color:var(--yellow);font-size:6.5px;text-align:center;letter-spacing:.5px;font-family:'Roboto',sans-serif}

/* programs */
.program{top:850px;height:150px;background:var(--card)}
.program-title{left:0;top:21px;width:100%;text-align:center;font-family:'Roboto',sans-serif;font-weight:500;font-size:12px;line-height:16px;color:var(--ink)}
.program-desc{left:10px;top:64px;width:140px;font-size:6px;line-height:10px;color:#333}
.program-btn{top:105px;width:75px;height:21px;border-radius:11px;background:var(--dark);color:var(--yellow);font-size:7px;text-align:center;line-height:21px;letter-spacing:.3px}

/* benefits */
.benefits{left:46px;top:1037px;width:279px;height:241px;background:var(--sky)}
.benefits-photo{left:325px;top:1037px;width:269px;height:241px;background:linear-gradient(180deg,#9ec3ea 0%,#c9dcec 45%,#8fa24e 70%,#6c7f35 100%)}
.benefits-title{left:22px;top:22px;font-family:'Roboto',sans-serif;font-weight:500;font-size:21px}
.benefits-list{left:34px;top:57px;list-style:none;font-size:10px;line-height:20px;color:#222}
.pill-dark{left:32px;top:193px;width:126px;height:21px;border:1.2px solid var(--ink);border-radius:11px;font-size:7px;text-align:center;line-height:18px;letter-spacing:.5px;font-family:'Roboto',sans-serif}

/* testimonial */
.avatar{left:295px;top:1363px;width:50px;height:50px;border-radius:50%;background:linear-gradient(180deg,#9a9a9a,#4d4d4d)}
.quote{left:130px;top:1429px;width:380px;text-align:center;color:var(--quote);font-size:11.5px;line-height:16px}
.quote-name{left:0;top:1497px;width:640px;text-align:center;color:var(--yellow-deep);font-size:11px}
.dots{left:292px;top:1532px;display:flex;gap:8px}
.dot{width:5px;height:5px;border-radius:50%;background:#d6dde6}
.dot.on{background:#35617f}

.clients{left:46px;top:1570px;width:548px;display:flex;justify-content:space-between;align-items:center}
.client{display:flex;align-items:center;gap:4px;font-family:'Roboto',sans-serif;font-weight:500;font-size:8px;color:#3a3a3a}
.client i{display:block;width:9px;height:9px;background:#3a3a3a}

.cta-band{left:0;top:1614px;width:640px;height:53px;background:var(--band);text-align:center;line-height:53px;font-family:'Roboto',sans-serif;font-weight:500;font-size:12px}

/* footer */
.footer{left:0;top:1667px;width:640px;height:265px;background:var(--dark);color:var(--white)}
.f-head{top:27px;font-family:'Roboto',sans-serif;font-weight:500;font-size:11px}
.f-links{left:47px;top:64px;list-style:none;font-size:7.5px;letter-spacing:.6px;color:var(--yellow)}
.f-links li{height:20px}
.f-text{font-size:6px;line-height:7.5px}
.f-tiny{font-size:4px;line-height:5px;color:#bbb}
.field{background:var(--field);color:#aaa;font-size:6.5px;padding:2px 4px;letter-spacing:.3px}
.btn-yellow{background:var(--yellow);color:var(--ink);border-radius:10px;font-size:6.5px;text-align:center;letter-spacing:.5px;font-family:'Roboto',sans-serif;font-weight:500}
.social{top:1842px;width:20px;height:20px;border-radius:50%;border:2px solid var(--white)}
</style>
</head>
<body>
<main class="page">
  <header class="site-header abs">
    <div class="brand abs"><span class="brand-mark"></span>STEADY MIND</div>
    <span class="nav abs nav-active" style="left:305px">Why me ?</span>
    <span class="nav abs" style="left:361px">Meet the Coach</span>
    <span class="nav abs" style="left:439px">Programs</span>
    <span class="nav abs" style="left:495px">Testimonials</span>
    <span class="nav abs" style="left:561px">Contact</span>
  </header>

  <section class="hero abs" role="img" aria-label="Photo of five smiling young friends sitting together, tinted blue"></section>
  <div class="hero-kicker abs" style="top:129px">LEARN TO SET YOUR</div>
  <div class="hero-title abs">STRESS</div>
  <div class="hero-kicker abs" style="top:189px">REDUCTION GOALS</div>
  <div class="hero-cta abs">CONTACT US</div>
  <div class="hero-rule abs"></div>

  <h1 class="section-title abs" style="top:356px">Welcome to SteadyMind</h1>
  <div class="intro abs">
    <p>Steady Mind came about due to my desire to help people lead a better and healthier life. Initially, I was involved in the fitness/body side of health. As years passed and my experience grew, I realized how important the mind was in total wellness, and that the mind is all powerful and controlling. Control the mind, control the body and achieve success. Stress can be the most debilating factor in our lives, it is the root cause of so many diseases and costs the US workplace an estimated 300 billion dollars due to loss of productivity.</p>
    <p>However stress is not all bad...we need stress to survive and peform at an optiomal level. In order to do that, you need to recognize your stressors and then control them, and put it to good use when neccsary. Stress is not all bad, and since we are surrounded by engulfed by stress, or it isn't going anywhere soon, we need to deal with it, and even better, channel to be an advantage/tool to perform better.</p>
    <p>Recognize when we are feeling stress and what is causing it, understand it, and how we react to it is the first step. Then when we sense it's coming we can deal with it, resolve it, or use it to our advantage. Effective stress control and problem solving skills may be the only thing that will keep your head above water in the next decade. It really is becoming quite serious and so should be taken very seriously. What is your plan for the next decade? Or, will you just let stress win?</p>
  </div>

  <div class="coach-photo abs" role="img" aria-label="Black and white portrait of the coach holding a coffee cup outdoors"></div>
  <section class="coach-panel abs">
    <h2 class="coach-name abs">The SteadyMind</h2>
    <p class="coach-text abs" style="top:59px">Been there done that! Have been through a lot, started businesses, selling a business, law suits, marriage, divorce, second marriage, kids, school, sports, fights, robbed, gun in face, traveled the world, successful, two great kids (both Cadets at Hillcrest Academy...duty/honor/country)</p>
    <p class="coach-text abs" style="top:126px">Limited number of clients...different stage of life, empty nester, have a full career...won't be a number</p>
    <div class="pill-outline abs" style="left:73px;top:180px;width:126px;height:21px;line-height:18px">SHARE YOUR STRESS</div>
  </section>

  <article class="program abs" style="left:46px;width:180px">
    <h3 class="program-title abs">Stress Management<br>Course for Individuals</h3>
    <p class="program-desc abs">Learn to use stress and anxiety reduction techniques.</p>
    <div class="program-btn abs" style="left:48px">Discover More</div>
  </article>
  <article class="program abs" style="left:227px;width:185px">
    <h3 class="program-title abs">Stress Reduction<br>Course for Organization</h3>
    <p class="program-desc abs">Give the gift of stress relief to your teams and members.</p>
    <div class="program-btn abs" style="left:60px">Discover More</div>
  </article>
  <article class="program abs" style="left:414px;width:180px">
    <h3 class="program-title abs">Stress Reduction<br>Course for Family</h3>
    <p class="program-desc abs">Stress relife programs for family members and couples.</p>
    <div class="program-btn abs" style="left:53px">Discover More</div>
  </article>

  <section class="benefits abs">
    <h2 class="benefits-title abs">Benefits</h2>
    <ul class="benefits-list abs">
      <li>Excellent listener with empathy</li>
      <li>Expertise in Health/ Wellness</li>
      <li>Mind/ Boody training</li>
      <li>Access professionals resources</li>
      <li>Sport psychologist consultancy</li>
      <li>Private confidentiality agreement</li>
    </ul>
    <div class="pill-dark abs">SHARE YOUR STRESS</div>
  </section>
  <div class="benefits-photo abs" role="img" aria-label="Photo of four friends walking through a grassy field under a blue sky"></div>

  <h2 class="section-title abs" style="top:1314px">Our Client Says</h2>
  <div class="avatar abs" role="img" aria-label="Client portrait"></div>
  <p class="quote abs">In enim justo, rhoncus ut, imperdiet a, venenatis vitae, justo. Nullam dictum felis eu pede mollis pretium. Integer tincidunt. Cras dapibus. Vivamus elementum semper nisi. Aenean vulputate eleifend tellus.</p>
  <div class="quote-name abs">Daniel Reyes</div>
  <div class="dots abs"><span class="dot"></span><span class="dot on"></span><span class="dot"></span><span class="dot"></span><span class="dot"></span></div>

  <div class="clients abs">
    <span class="client"><i></i>Northway Health</span>
    <span class="client">Valor MBA</span>
    <span class="client">Kestrel</span>
    <span class="client">Coach Guild</span>
    <span class="client">Larchline</span>
    <span class="client"><i></i>Mesa State University</span>
  </div>

  <div class="cta-band abs">Tell us about you and your stress reduction goals for your workplace, school or organization.</div>

  <footer class="footer abs">
    <h4 class="f-head abs" style="left:46px">Quick Links</h4>
    <ul class="f-links abs">
      <li>STESS COURSE FOR INDIVIDUALS</li>
      <li>FAMILY STESS COURSE PROGRAMES</li>
      <li>COURSES FOR ORGANIZATION</li>
      <li>ONLINE COURSES</li>
      <li>TERMS &amp; CONDITIONS</li>
      <li>PRIVACY POLICY</li>
    </ul>

    <h4 class="f-head abs" style="left:232px">Share Your Stress</h4>
    <p class="f-text abs" style="left:234px;top:62px;width:152px">Share your stress and set stress reduction goals for your workplace, school or organization.</p>
    <p class="f-tiny abs" style="left:233px;top:82px;width:152px">Feel free to share your data with our team. We keep your data safe and maintain standard privacy rules.</p>
    <div class="field abs" style="left:233px;top:103px;width:152px;height:13px">Your Name</div>
    <div class="field abs" style="left:233px;top:126px;width:152px;height:13px">Your Contact Number</div>
    <div class="field abs" style="left:233px;top:149px;width:152px;height:44px">Describe your problem in details ...</div>
    <div class="btn-yellow abs" style="left:233px;top:206px;width:67px;height:19px;line-height:19px">SUBMIT</div>

    <h4 class="f-head abs" style="left:418px">More Information</h4>
    <p class="f-text abs" style="left:418px;top:62px;width:160px">Please subscribe to get upto date information about our latest course, resources, news and more.</p>
    <div class="field abs" style="left:418px;top:86px;width:152px;height:14px"></div>
    <p class="f-tiny abs" style="left:418px;top:106px;width:168px">By submitting this form, you are consenting to receive marketing emails. You can revoke your consent to receive emails at any time by using Unsubscribe link, found at the bottom of every email.</p>
    <div class="btn-yellow abs" style="left:418px;top:131px;width:152px;height:19px;line-height:19px">SUBSCRIBE</div>
  </footer>
  <span class="social abs" style="left:420px" role="img" aria-label="Social link"></span>
  <span class="social abs" style="left:452px" role="img" aria-label="Social link"></span>
  <span class="social abs" style="left:484px" role="img" aria-label="Social link"></span>
  <span class="social abs" style="left:516px" role="img" aria-label="Social link"></span>
</main>
</body>
</html>
```